Northwind Harbor Capital Business Card

Creativity is a must. We'd prefer something different from the run of the mill.

The emphasis in our name is on Harbor. We'd like to see some vertical designs.

I've added a copy of our logo and the QR code we'd like to use. Our tag line is A QUIET HAND ON EVERY VENTURE™

Business Card Data
Name: Ron Vickers
Address: 24519 Palmetto Ridge Rd, Odessa, FL 33556
Main: 813-555-0142
Cell: 813-555-0187
Fax: 813-555-0163
Email: rvickers@northwindharbor.example
URL: www.northwindharbor.example

We use Printlyx.com for our business cards and will need a fully editable psd file using their template.

Target Market(s)

We need a new business card design for a US based private equity firm. Our clients are investors and business owners.

Industry/Entity Type

Business

Font styles to use
Sans Serif

Requirements
Must have
• QR code
Creativity
You're welcome to change the logo color palette

```html
<!DOCTYPE html>
<html lang="en">
<head>
<meta charset="utf-8">
<title>Northwind Harbor Capital – Business Card</title>
<link rel="stylesheet" href="https://fonts.googleapis.com/css2?family=Exo+2:ital,wght@0,400;0,500;1,600&display=swap">
<style>
  :root {
    --stage: #e9ebee;
    --card: #fbfbfc;
    --band: #2f6cc4;
    --navy: #1f2f63;
    --ink: #3a3d44;
    --accent: #2f6cc4;
    --qr: #d9dee6;
  }
  * { box-sizing: border-box; margin: 0; padding: 0; }
  html, body { width: 1200px; height: 1059px; overflow: hidden; }
  body {
    background: var(--stage);
    font-family: "Exo 2", sans-serif;
    color: var(--ink);
    position: relative;
  }
  .card {
    position: absolute;
    top: 374px;
    width: 540px;
    height: 310px;
    background: var(--card);
    border-radius: 4px;
    box-shadow: 0 6px 18px rgba(30, 40, 60, 0.14);
    overflow: hidden;
  }
  .card--back { left: 40px; }
  .card--front { left: 620px; }

  .bands { position: absolute; inset: 0; }

  .wordmark {
    position: absolute;
    display: flex;
    align-items: center;
    gap: 12px;
    color: var(--navy);
    font-weight: 500;
    letter-spacing: 0.14em;
    text-transform: uppercase;
    line-height: 1.05;
  }
  .wordmark__square { width: 16px; height: 16px; background: var(--navy); flex: none; }
  .wordmark__lines { display: flex; flex-direction: column; }
  .wordmark__key { font-size: 1.6em; letter-spacing: 0.08em; }

  .card--back .wordmark { left: 28px; top: 14px; font-size: 12px; }
  .card--front .brand {
    position: absolute;
    left: 50%; top: 50%;
    transform: translate(-50%, -50%);
    display: flex;
    flex-direction: column;
    align-items: flex-start;
    gap: 16px;
  }
  .card--front .wordmark { position: static; font-size: 22px; gap: 18px; }
  .card--front .wordmark__square { width: 26px; height: 26px; }
  .tagline {
    font-size: 11px;
    letter-spacing: 0.16em;
    color: var(--accent);
    text-transform: uppercase;
    padding-left: 44px;
  }

  .holder { position: absolute; left: 330px; top: 124px; }
  .holder__name {
    font-style: italic;
    font-weight: 600;
    font-size: 22px;
    letter-spacing: 0.04em;
    color: var(--accent);
    text-transform: uppercase;
  }
  .holder__role {
    font-size: 12px;
    letter-spacing: 0.16em;
    text-transform: uppercase;
    margin-top: 2px;
  }
  .address {
    position: absolute;
    left: 28px;
    top: 132px;
    font-size: 11px;
    width: 220px;
    line-height: 1.4;
  }

  .contacts {
    position: absolute;
    left: 28px;
    top: 204px;
    list-style: none;
    font-size: 12px;
    line-height: 1;
  }
  .contacts li { display: flex; align-items: center; gap: 8px; margin-bottom: 6px; }
  .contacts svg { width: 12px; height: 12px; fill: var(--accent); flex: none; }
  .contacts__label { width: 30px; color: var(--navy); font-weight: 500; }

  .qr {
    position: absolute;
    right: 28px;
    bottom: 22px;
    width: 76px;
    height: 76px;
    background: var(--qr);
    border: 4px solid var(--navy);
  }
</style>
</head>
<body>

<section class="card card--back" aria-label="Card back">
  <svg class="bands" viewBox="0 0 540 310" aria-hidden="true">
    <path d="M0 98 H245 L285 142 L325 98 H540" fill="none" stroke="var(--band)" stroke-width="30" stroke-linejoin="miter"/>
    <path d="M0 180 H245 L285 224 L325 180 H540" fill="none" stroke="var(--band)" stroke-width="20" stroke-linejoin="miter"/>
  </svg>

  <div class="wordmark">
    <span class="wordmark__square"></span>
    <span class="wordmark__lines"><span>Northwind</span><span class="wordmark__key">Harbor</span><span>Capital</span></span>
  </div>

  <div class="holder">
    <p class="holder__name">Ron Vickers</p>
    <p class="holder__role">Financial Advisor</p>
  </div>

  <p class="address">24519 Palmetto Ridge Rd, Odessa, FL 33556</p>

  <ul class="contacts">
    <li><svg viewBox="0 0 24 24"><path d="M6.6 10.8a15 15 0 0 0 6.6 6.6l2.2-2.2c.3-.3.7-.4 1-.2 1.1.4 2.3.6 3.6.6.6 0 1 .4 1 1V20c0 .6-.4 1-1 1A17 17 0 0 1 3 4c0-.6.4-1 1-1h3.5c.6 0 1 .4 1 1 0 1.3.2 2.5.6 3.6.1.3 0 .7-.2 1z"/></svg><span class="contacts__label">Main</span>813-555-0142</li>
    <li><svg viewBox="0 0 24 24"><path d="M7 1h10a2 2 0 0 1 2 2v18a2 2 0 0 1-2 2H7a2 2 0 0 1-2-2V3a2 2 0 0 1 2-2zm0 3v14h10V4z"/></svg><span class="contacts__label">Cell</span>813-555-0187</li>
    <li><svg viewBox="0 0 24 24"><path d="M6 2h10l4 4v6H6zM3 12h18v8H3zm3 3v2h4v-2z"/></svg><span class="contacts__label">Fax</span>813-555-0163</li>
    <li><svg viewBox="0 0 24 24"><path d="M2 5h20v14H2zm2 2v.5l8 5 8-5V7z"/></svg>rvickers@northwindharbor.example</li>
    <li><svg viewBox="0 0 24 24"><circle cx="12" cy="12" r="10"/></svg>www.northwindharbor.example</li>
  </ul>

  <div class="qr" role="img" aria-label="QR code linking to www.northwindharbor.example"></div>
</section>

<section class="card card--front" aria-label="Card front">
  <div class="brand">
    <div class="wordmark">
      <span class="wordmark__square"></span>
      <span class="wordmark__lines"><span>Northwind</span><span class="wordmark__key">Harbor</span><span>Capital</span></span>
    </div>
    <p class="tagline">A Quiet Hand on Every Venture™</p>
  </div>
</section>

</body>
</html>
```